Guaranteed Job - Sleek Sexy Business Card UV Spot

Im looking for a sleek and sexy business card, that resembles elite or VIP status status.
our business is corinvale.example
you can view our products on there, but our main audience for handing out our cards will be for people in the hospitality industry, so it will need to impress high management and CEO of hotels and restaurants, bars, clubs etc...
the card features will have UV spot on both sides, 400gsm stock. standard size.
Artwork should be 86 x 54mm + 2mm bleed = 90 x 58mm
it should have a nice "unique" uv spot pattern that highlights the card, not a repeated pattern, theres no originality there, and it will be disregarded.
The written material will be:
Corin Vale Hospitality College (logo)
Tobin Marsh
Director
Phone: 1300 615 737
Mobile: 0455 817 296
Email: info@corinvale.example
website: www.corinvale.example
I'm looking for originality here, i don't want just a simple stock card, want something that has a wow factor for people.
You will find the logo attached. you may invert the white to black words to suit the background as you please.
thank you and good luck
As a side note, ive received a lot of proposals, im too busy to give feedback to each and every one, so if i havent provided feedback for your design within 24 hours, then consider it not acceptable, and you could resubmit another design.
So far i have not seen any design that stood out for me, they all seem pretty generic. there nothing thats unique, i would figure for the amount that im offering, that people would put some more effort and creativity into the design.
so far over 200 designs submitted, and nothing i have seen looks very original, everything looks like a different variation of the same stuff, i said it very clearly i wanted something unique, the only thing that has come close to it so far is this one
Reason: Ive received alot of design concepts and i have reviewed everyone, but i havent had time to give feedback to every single one, only the ones that have interested me, if i havent responded, its because i havent found it good enough.
so far only a few design have been on par with what ive been looking for, an attractive eye popping design.
heres a few of them,
http://files.pixelbazaar.example/design_img/51736/62418/62418_2840915_51736_image.jpg
http://files.pixelbazaar.example/design_img/51736/68254/68254_2841377_51736_image.jpg
theyre, both unique and original, and eye catching, the only thing theyre missing is the sexyness.
if you still think you have some creativity left in your minds, then throw it on here.
Reason: Sorry guys for the delay, I was in a serious accident and out of commission for the past few months, I'm just slowly recovering now, please bare with me as i try to attend to this project, it may take me awhile as I have other projects that are on standby, I'm not 100% at the moment, so im extending the deadline for 2 weeks right now. Thanks for your patience.
Hospitality

```html
<!DOCTYPE html>
<html lang="en">
<head>
<meta charset="utf-8">
<title>Corin Vale Hospitality College – Business Card</title>
<link rel="stylesheet" href="https://fonts.googleapis.com/css2?family=Maven+Pro:wght@400;600;700&display=swap">
<style>
  :root {
    --sky: #6db1e2;
    --sky-deep: #5aa2d6;
    --ink: #030303;
    --white: #ffffff;
    --backdrop: #e9e7e3;
    --label: #6db1e2;
  }
  * { box-sizing: border-box; margin: 0; padding: 0; }
  html, body {
    width: 1200px; height: 900px; overflow: hidden;
    background: var(--backdrop);
    font-family: "Maven Pro", Arial, sans-serif;
  }
  .sheet {
    width: 1200px; height: 900px;
    display: flex; align-items: center; justify-content: center; gap: 60px;
  }
  .card {
    position: relative;
    width: 516px; height: 324px;
    background: var(--sky);
    border-radius: 4px;
    box-shadow: 0 10px 26px rgba(0,0,0,.18);
    overflow: hidden;
  }
  .card__panel {
    position: absolute;
    left: 14px; top: 24px; right: 42px; bottom: 20px;
    background: var(--ink);
    border-radius: 16px 46px 46px 16px;
  }
  .brand {
    position: absolute;
    right: 28px; top: 40px;
    display: flex; align-items: center; gap: 12px;
    color: var(--white);
  }
  .card--back .brand { top: 110px; right: 50px; }
  .brand__mark {
    width: 30px; height: 30px; background: var(--sky);
  }
  .brand__name {
    font-weight: 700; font-size: 16px; line-height: 1.1;
    text-transform: uppercase; letter-spacing: .02em;
    width: 150px;
  }
  .contact {
    position: absolute;
    left: 26px; bottom: 28px; right: 24px;
    display: flex; gap: 26px; align-items: flex-end;
    color: var(--white); font-size: 12.5px; line-height: 1.55;
  }
  .contact__person { min-width: 190px; }
  .contact__name {
    font-weight: 700; font-size: 22px; color: var(--sky);
    line-height: 1.2;
  }
  .contact__role {
    font-weight: 400; font-size: 12.5px; color: var(--white);
    padding-left: 4px;
  }
  .contact__role::before { content: "| "; color: #bbb; }
  .contact__label { color: var(--label); }
</style>
</head>
<body>
  <main class="sheet">
    <section class="card card--back" aria-label="Card back">
      <div class="card__panel">
        <div class="brand">
          <span class="brand__mark"></span>
          <span class="brand__name">Corin Vale Hospitality College</span>
        </div>
      </div>
    </section>

    <section class="card card--front" aria-label="Card front">
      <div class="card__panel">
        <div class="brand">
          <span class="brand__mark"></span>
          <span class="brand__name">Corin Vale Hospitality College</span>
        </div>
        <div class="contact">
          <div class="contact__person">
            <div class="contact__name">Tobin Marsh<span class="contact__role">Director</span></div>
            <div><span class="contact__label">Phone:</span> 1300 615 737</div>
            <div><span class="contact__label">Mobile:</span> 0455 817 296</div>
          </div>
          <div class="contact__web">
            <div><span class="contact__label">Email:</span> info@corinvale.example</div>
            <div><span class="contact__label">Web:</span> www.corinvale.example</div>
            <div>&nbsp;</div>
          </div>
        </div>
      </div>
    </section>
  </main>
</body>
</html>
```